Email Signature Design

Please design an email signature, the below is an example of our current design;
___

CARRODY ESTATE HOLDINGS PTY LTD
BENEDICT HARLOWE
Licensed Strata and Community Manager

143 Tallowood Street,
KELDARRA NSW 2093

P: 02.9473.6820 F: 9536.2048
Website: www.carrodyestate.com.au

This e-mail message and accompanying data may contain information that is confidential and private. If you are not the intended recipient, the use, dissemination, distribution or copying of this message or data is prohibited.

If you have received this e-mail in error please notify us immediately and delete all material pertaining to this e-mail. strata@carrodyestate.com.au

___

We would like to incorporate our logo and company colours, you can view the colours and feel of image at www.carrodyestate.com.au

Industry/Entity Type

It Company

Requirements
Must have
• use of logo and company colours (image)

```html
<!DOCTYPE html>
<html lang="en">
<head>
<meta charset="utf-8">
<title>Carrody Estate Holdings – Email Signature</title>
<link href="https://fonts.googleapis.com/css2?family=Arimo:wght@400;700&display=swap" rel="stylesheet">
<style>
  :root {
    --olive: #4f5a2b;
    --olive-dark: #3f4a22;
    --rule: #cbc196;
    --ink: #3d3d3d;
    --ink-soft: #4a4a4a;
    --charcoal: #3b3b3b;
    --paper: #ffffff;
  }
  * { margin: 0; padding: 0; box-sizing: border-box; }
  html, body {
    width: 1200px; height: 900px; overflow: hidden;
    background: var(--paper);
    font-family: "Arimo", Arial, sans-serif;
    color: var(--ink);
  }
  .signature {
    position: absolute; left: 77px; top: 243px; width: 486px;
  }
  .brand {
    display: flex; align-items: flex-end; gap: 10px; height: 84px;
  }
  .brand-square {
    width: 54px; height: 54px; background: var(--olive); flex: none;
  }
  .brand-name {
    font-weight: 700; font-size: 12px; letter-spacing: 0.2px;
    color: var(--charcoal); line-height: 1.2; padding-bottom: 1px;
  }
  .rule {
    height: 2px; background: var(--rule); width: 486px;
  }
  .rule-top { margin-top: 18px; }
  .person { padding-top: 9px; padding-bottom: 30px; }
  .person-name {
    font-weight: 700; font-size: 24px; letter-spacing: 0.6px;
    color: var(--olive); line-height: 28px;
  }
  .person-role, .person-phone {
    font-size: 17px; letter-spacing: 0.5px; color: var(--ink-soft);
    line-height: 27px;
  }
  .company { padding-top: 11px; }
  .company-name {
    font-weight: 700; font-size: 22.5px; letter-spacing: 0.6px;
    color: var(--olive); line-height: 28px;
  }
  .company-details {
    display: flex; margin-top: 15px; font-size: 17px; letter-spacing: 0.4px;
    line-height: 25px; color: var(--ink-soft);
  }
  .address { width: 216px; }
  .contact { white-space: nowrap; }
  .contact b { font-weight: 700; }
  .website { color: var(--olive); }
  .disclaimer {
    margin-top: 15px; font-size: 10px; line-height: 12.5px; color: var(--ink);
    width: 486px;
  }
  .disclaimer .email { color: var(--olive); }
</style>
</head>
<body>
  <section class="signature">
    <div class="brand">
      <span class="brand-square" aria-hidden="true"></span>
      <span class="brand-name">CARRODY ESTATE<br>STRATA MANAGEMENT SERVICES</span>
    </div>

    <div class="rule rule-top"></div>
    <div class="person">
      <p class="person-name">BENEDICT HARLOWE</p>
      <p class="person-role">Licensed Strata and Community Manager</p>
      <p class="person-phone">02.9473.6820 x101</p>
    </div>

    <div class="rule"></div>
    <div class="company">
      <p class="company-name">CARRODY ESTATE HOLDINGS PTY LTD</p>
      <div class="company-details">
        <p class="address">143 Tallowood Street,<br>Keldarra, NSW 2093</p>
        <p class="contact"><b>P:</b> 02.9473.6820 | <b>F:</b> 9536.2048<br><span class="website">www.carrodyestate.com.au</span></p>
      </div>
    </div>

    <p class="disclaimer">This e-mail message and accompanying data may contain information that is confidential and private.<br>If you are not the intended recipient, the use, dissemination, distribution or copying of this message or data<br>is prohibited. If you have received this e-mail in error please notify us immediately and delete all material<br>pertaining to this e-mail <span class="email">strata@carrodyestate.com.au</span></p>
  </section>
</body>
</html>
```